■依頼の目的/概要
ハルカゼのlumoraで電子書籍出版をします。

■本の内容
40代女性で話すことや伝えること
自分に自信はないけれど

起業したい、
夢や目標を叶えたい、
という方がターゲットです。

声と潜在意識(心)の力を使う「ひだまりトーン」で
人前で自信をもって伝えられるようになったり
やりたいことがどんどん実現できるようになる方法を
書きました。

声や潜在意識を使ったトレーニング、
実例を用いてお伝えしています。

■デザイン要望
40代女性が好むデザインが希望です。
顔写真も入れていただけたらと思います。
その際、手に持っている音符などは載せないようお願いいたします。

お写真と、電子書籍の文章をお送りいたします。

ご応募、心よりお待ちしております!!!

その他何かご不明な点がございましたら、お気軽にご質問下さい。
よろしくお願いいたします。
タイトルは
響きの名手がひもとく
輝く毎日をつくる心の整え方・磨き方
~ひだまりトーンの秘密~

著者は
ひだまりトーンコンサルタント
さとうれな

どうぞよろしくお願いいたします。
LQS表記では、表紙画像のサイズは 50 MB 未満表紙フ
ァイルの理想的な寸法は 2,560 x 1,600 ピクセルとなっています。

文字が見やすいこと。
女性的な優しいイメージと内容が合うもの、
という視点で選ばせていただきました。

素晴らしい作品ばかりで
選ばせていただくのに時間がかかりました。

短期間にも関わらず
素敵な作品を沢山ご応募いただき
どうもありがとうございました!

心より感謝いたします。

機会がございましたら
またどうぞよろしくお願いいたします。

```html
<!DOCTYPE html>
<html lang="ja">
<head>
<meta charset="utf-8">
<title>輝く毎日をつくる心の整え方・磨き方</title>
<link rel="stylesheet" href="https://fonts.googleapis.com/css2?family=Noto+Sans+JP:wght@500;700;900&display=swap">
<style>
  :root{
    --gold:#c9a45c;
    --gold-light:#e6cf97;
    --brown:#4a2f22;
    --brown-deep:#3a2219;
    --ink:#2a2320;
    --pink:#e0457b;
    --paper:#ffffff;
    --blush-1:#f3ddd6;
    --blush-2:#e9c8bd;
    --blush-3:#d9b2a6;
  }
  *{margin:0;padding:0;box-sizing:border-box}
  html,body{width:750px;height:1200px;overflow:hidden;background:var(--paper)}
  body{font-family:"Noto Sans JP",sans-serif;color:var(--ink)}
  .cover{position:relative;width:750px;height:1200px;overflow:hidden;background:var(--paper)}
  .backdrop-photo{
    position:absolute;left:0;top:0;width:750px;height:720px;
    background:
      radial-gradient(ellipse 260px 320px at 560px 330px,#e4bfb3 0%,rgba(228,191,179,0) 70%),
      linear-gradient(160deg,var(--blush-1) 0%,var(--blush-2) 45%,var(--blush-3) 100%);
  }
  .lower-fade{
    position:absolute;left:0;top:560px;width:750px;height:200px;
    background:linear-gradient(to bottom,rgba(255,255,255,0),var(--paper) 80%);
  }
  .title-panel{
    position:absolute;left:40px;top:190px;width:670px;height:380px;
    background:rgba(255,255,255,.72);
  }
  .frame{position:absolute;inset:0;pointer-events:none}
  .catch{
    position:absolute;left:50%;top:158px;transform:translateX(-50%);
    background:var(--brown-deep);color:#fff;font-weight:700;font-size:30px;
    padding:10px 30px;border-radius:10px;white-space:nowrap;letter-spacing:.02em;
  }
  .catch::after{
    content:"";position:absolute;left:50%;bottom:-16px;transform:translateX(-50%);
    border:10px solid transparent;border-top:8px solid var(--brown-deep);border-bottom:0;
    width:0;height:0;border-width:16px 12px 0 12px;border-color:var(--brown-deep) transparent transparent transparent;
  }
  .title-lead{
    position:absolute;left:0;width:750px;top:262px;text-align:center;
    font-weight:900;font-size:50px;letter-spacing:.02em;color:var(--ink);
  }
  .title-main{
    position:absolute;left:0;width:750px;top:335px;text-align:center;
    font-weight:900;font-size:88px;line-height:1.12;color:var(--ink);letter-spacing:.01em;
  }
  .series-band{
    position:absolute;left:110px;top:628px;width:530px;height:66px;
    background:var(--brown);border-radius:12px;
    color:var(--gold-light);font-weight:700;font-size:36px;
    display:flex;align-items:center;justify-content:center;letter-spacing:.04em;
  }
  .bonus{position:absolute;left:78px;top:725px;width:440px}
  .bonus-heading{color:var(--pink);font-weight:900;font-size:38px;margin-bottom:12px}
  .bonus-list{list-style:none;font-weight:700;font-size:24px;line-height:1.5;color:var(--ink)}
  .bonus-list li{margin-bottom:4px}
  .bonus-list .sub{display:block;padding-left:24px}
  .author-photo{
    position:absolute;left:518px;top:793px;width:164px;height:164px;border-radius:50%;
    background:radial-gradient(circle at 50% 40%,#f4e6e0 0%,#e2c7bc 55%,#b99a8d 100%);
  }
  .author{position:absolute;left:0;width:750px;top:1098px;text-align:center}
  .author-role{font-weight:700;font-size:22px;color:var(--ink);padding-left:120px}
  .author-name{font-weight:700;font-size:34px;color:var(--ink);margin-top:6px;padding-left:120px}
  .author-name small{font-size:22px;margin-right:10px}
</style>
</head>
<body>
<main class="cover">
  <div class="backdrop-photo" role="img" aria-label="柔らかなピンクベージュ調の女性のポートレート写真"></div>
  <div class="lower-fade"></div>
  <div class="title-panel"></div>

  <svg class="frame" width="750" height="1200" viewBox="0 0 750 1200" aria-hidden="true">
    <rect x="22" y="22" width="706" height="1156" fill="none" stroke="var(--gold)" stroke-width="5"/>
    <rect x="34" y="34" width="682" height="1132" fill="none" stroke="var(--gold)" stroke-width="1.5"/>
  </svg>

  <div class="catch">響きの名手がひもとく</div>

  <h1>
    <span class="title-lead">輝く毎日をつくる</span>
    <span class="title-main">心の整え方・<br>磨き方</span>
  </h1>

  <div class="series-band">ひだまりトーンの秘密</div>

  <section class="bonus">
    <h2 class="bonus-heading">3大特典をプレゼント</h2>
    <ul class="bonus-list">
      <li>★ガラリと変わる!<span class="sub">願いを叶えるアファメーション小冊子</span></li>
      <li>★ひだまりトーン診断<span class="sub">(あなたの声は売れ声?ダメ声?)</span></li>
      <li>★本書の解説付!特別レッスン動画30分</li>
    </ul>
  </section>

  <div class="author-photo" role="img" aria-label="著者のポートレート写真"></div>

  <div class="author">
    <p class="author-role">ひだまりトーンコンサルタント</p>
    <p class="author-name"><small>著者:</small>さとうれな</p>
  </div>
</main>
</body>
</html>
```